BeatHarbor.com

We would like all designers to build a entertainment social networking website that will display exclusive content. The content will also consist of interviews of local and national recording artist and entertainers from various genre. Our site will also have concert footage, behind the scene footage. Our site will be used in conjunction with ZORVEX software so we want all designer to take a look at their layout at zorvex.com We would like our website to have a unique design, the main sections of our website are the following:

Social Networking Page for Artist, Entertainers and Innovators
The Proving Yard
Crown Climber Series
Networking Events –Bright Spark Talent Show
Exclusive Content
Event Promotion
Artist Profiles (Music, Music Videos, Portfolios)
Updates

I have included our logo. Please incorporate with your designs!

Thank You!

This is a general post for all designrs. I uploaded several diiferent pages that I would like completed please let me know if you dont have any of the following pages.

artist on the rise
provingyrad
profile
homepage

Thank You!

Reason: All pages havent been completed! Also had issues getting documentation to designers, was unaware they didnt have information in full!

The home page, The artist of the month page, the proving yard page, the members page are all individual pages. We need designers to create all of these individual pages so we judge which one we like the most.
We have extended the deadline to give you all more time to design The home page, The artist of the month page, the proving yard page, the members page. Please contact us if you have any questions. Thanks Beat Harbor

Reason: Designers have not completed all the pages described in our brief description

Reason: We are almost finished with the site but we did notice a few things we need to add to the pages

Reason: we need the right files delivered for our website

Target Market(s)

Our target market is male and female ages 13-30 that are interested in the media and entertainment business. We welcome all genres of entertainment including, mobile app developer, independent filmmakers, musicians, etc

Industry/Entity Type

Entertainment

Requirements
Must have
• Our site must have a music/entertainment feel to it. We want a design that communicates success.
Nice to have
• Glossy, slick design

```html
<!DOCTYPE html>
<html lang="en">
<head>
<meta charset="utf-8">
<title>Beat Harbor — Members</title>
<link href="https://fonts.googleapis.com/css2?family=Bebas+Neue&family=Noto+Serif:wght@400;700&family=Arimo:wght@700&display=swap" rel="stylesheet">
<style>
  :root {
    --page-bg: #1e1e1e;
    --page-bg-dark: #121212;
    --panel: #030303;
    --panel-edge: #2c2c2c;
    --gold: #e8a24a;
    --gold-deep: #b0701e;
    --nav-top: #f2f2f2;
    --nav-bottom: #d3d3d3;
    --nav-text: #1a1a1a;
    --nav-active: #a8701c;
    --nav-divider: #c4c4c4;
    --light-text: #f0f0f0;
    --footer-text: #e6e6e6;
    --thumb-warm: #c9a48a;
    --thumb-frame: #d88a3c;
  }
  * { margin: 0; padding: 0; box-sizing: border-box; }
  html, body { width: 1200px; height: 900px; overflow: hidden; }
  body {
    position: relative;
    background: radial-gradient(ellipse at 50% 30%, #2a2a2a 0%, var(--page-bg) 45%, var(--page-bg-dark) 100%);
    font-family: "Noto Serif", serif;
  }
  .abs { position: absolute; }

  /* Brand pennant */
  .brand-pennant { left: 110px; top: 0; width: 192px; height: 242px; }
  .brand-mark {
    left: 110px; top: 64px; width: 192px; display: flex; flex-direction: column; align-items: center; gap: 14px;
  }
  .brand-dot { width: 74px; height: 74px; border-radius: 50%; background: var(--gold-deep); }
  .brand-name { font-family: "Noto Serif", serif; font-size: 15px; color: var(--gold); letter-spacing: 0.5px; }

  /* Navigation */
  .main-nav {
    left: 324px; top: 0; width: 766px; height: 78px;
    background: linear-gradient(var(--nav-top), var(--nav-bottom));
    display: flex; align-items: center;
  }
  .main-nav a {
    font-family: "Noto Serif", serif; font-weight: 700; font-size: 12.5px; letter-spacing: 0.6px;
    color: var(--nav-text); text-decoration: none; height: 78px; display: flex; align-items: center; justify-content: center;
    border-right: 1px solid var(--nav-divider);
  }
  .main-nav a:last-child { border-right: none; }
  .main-nav a.is-active { color: var(--nav-active); }

  /* Hero */
  .hero {
    left: 324px; top: 105px; width: 766px; height: 346px; border: 1px solid #3a3a3a; overflow: hidden;
  }
  .hero-photo {
    position: absolute; inset: 0;
    background: radial-gradient(ellipse at 45% 45%, #7a7a7a 0%, #4b4b4b 35%, #232323 70%, #111 100%);
  }
  .hero-title {
    left: 24px; top: 28px; font-family: "Bebas Neue", sans-serif; font-size: 66px; line-height: 70px; color: #050505;
    text-shadow: -2px -2px 0 #ddd, 2px -2px 0 #ddd, -2px 2px 0 #ddd, 2px 2px 0 #ddd;
  }
  .hero-sub {
    left: 24px; top: 252px; font-family: "Arimo", sans-serif; font-weight: 700; font-size: 21px; line-height: 31px; color: var(--light-text);
    text-shadow: 0 0 3px #000, 1px 1px 0 #000;
  }
  .video-player { left: 429px; top: 26px; width: 299px; height: 251px; background: #000; border: 1px solid #444; }
  .player-play {
    left: 124px; top: 100px; width: 50px; height: 34px; border-radius: 6px;
    background: linear-gradient(#e4e4e4, #8a8a8a); display: flex; align-items: center; justify-content: center;
  }
  .player-brand { right: 6px; top: 206px; font-family: "Arimo", sans-serif; font-size: 14px; color: #bbb; }
  .player-bar {
    left: 0; bottom: 0; width: 297px; height: 17px; background: linear-gradient(#f2f2f2, #c8c8c8);
    display: flex; align-items: center; font-family: "Arimo", sans-serif; font-size: 8px; color: #222;
  }
  .player-track { width: 176px; height: 5px; margin: 0 8px 0 14px; background: #999; border-radius: 3px; }

  /* Members sidebar */
  .members-panel { left: 110px; top: 296px; width: 192px; height: 432px; }
  .section-title {
    font-family: "Bebas Neue", sans-serif; font-size: 25px; letter-spacing: 0.5px;
    background: linear-gradient(#f7c27a, var(--gold-deep)); -webkit-background-clip: text; background-clip: text; color: transparent;
  }
  .members-title { left: 110px; top: 339px; width: 192px; text-align: center; }
  .member-grid {
    left: 137px; top: 389px; display: grid; grid-template-columns: repeat(3, 42px); column-gap: 5px; row-gap: 4px;
  }
  .member-thumb {
    width: 42px; height: 29.7px; border: 1px solid var(--thumb-frame);
    background: linear-gradient(135deg, #eee 0%, var(--thumb-warm) 55%, #7a4a2c 100%);
  }

  /* Video section */
  .video-panel {
    left: 325px; top: 500px; width: 764px; height: 228px; background: var(--panel); border: 1px solid var(--panel-edge);
  }
  .video-title { left: 358px; top: 521px; }
  .video-row { left: 356px; top: 571px; display: flex; gap: 18px; }
  .video-thumb {
    position: relative; width: 163px; height: 104px; border: 1px solid #bbb;
    background: linear-gradient(160deg, #7d7b5e 0%, #55533d 45%, #3a3628 100%);
  }
  .thumb-play {
    position: absolute; left: 56px; top: 32px; width: 37px; height: 39px; background: rgba(200,200,200,0.55);
    display: flex; flex-direction: column; align-items: center; justify-content: center;
    font-family: "Arimo", sans-serif; font-size: 6px; color: #eee;
  }

  /* Footer */
  .footer-rule { left: 0; top: 826px; width: 1200px; height: 2px; background: #333; border-top: 1px solid #0a0a0a; }
  .footer-links {
    left: 112px; top: 849px; display: flex; align-items: center; font-size: 11px; color: var(--footer-text);
  }
  .footer-links a { color: var(--footer-text); text-decoration: none; }
  .footer-links .sep { margin: 0 3px 0 4px; }
  .social { display: flex; gap: 2px; margin-left: 11px; }
  .social span { width: 27px; height: 27px; border-radius: 4px; background: #5b6f8f; }
</style>
</head>
<body>

  <svg class="abs brand-pennant" viewBox="0 0 192 242" aria-hidden="true">
    <defs>
      <linearGradient id="pennantFill" x1="0" y1="0" x2="0" y2="1">
        <stop offset="0" stop-color="#151515"/><stop offset="1" stop-color="#000"/>
      </linearGradient>
    </defs>
    <polygon points="0,0 192,0 192,160 96,240 0,160" fill="url(#pennantFill)" stroke="#333" stroke-width="1"/>
  </svg>
  <div class="abs brand-mark">
    <span class="brand-dot"></span>
    <span class="brand-name">Beat Harbor</span>
  </div>

  <nav class="abs main-nav">
    <a href="#" class="is-active" style="width:109px">MEMBERS</a>
    <a href="#" style="width:141px">PROVING YARD</a>
    <a href="#" style="width:199px">ARTIST OF THE MONTH</a>
    <a href="#" style="width:317px">CROWN CLIMBER SERIES - COMING SOON</a>
  </nav>

  <section class="abs hero">
    <div class="hero-photo" role="img" aria-label="Black and white close-up photo of studio headphones"></div>
    <h1 class="abs hero-title">SED UT<br>PERSPICIATIS<br>UNDE</h1>
    <p class="abs hero-sub">veritatis et quasi architecto<br>beatae vitae dicta</p>
    <div class="abs video-player">
      <div class="abs player-play">
        <svg width="16" height="16" viewBox="0 0 16 16"><polygon points="3,1 14,8 3,15" fill="#333"/></svg>
      </div>
      <span class="abs player-brand">ClipRiver</span>
      <div class="abs player-bar">
        <svg width="16" height="17" viewBox="0 0 16 17"><polygon points="5,4 12,8.5 5,13" fill="#222"/></svg>
        <span class="player-track"></span>
        <span>0:00 / 0:00</span>
      </div>
    </div>
  </section>

  <svg class="abs members-panel" viewBox="0 0 192 432" aria-hidden="true">
    <polygon points="0,28 66,28 96,0 126,28 192,28 192,432 0,432" fill="var(--panel)" stroke="#2c2c2c" stroke-width="1.5"/>
  </svg>
  <h2 class="abs section-title members-title">MEMBERS</h2>
  <div class="abs member-grid">
    <span class="member-thumb" role="img" aria-label="Member photo"></span><span class="member-thumb" role="img" aria-label="Member photo"></span><span class="member-thumb" role="img" aria-label="Member photo"></span>
    <span class="member-thumb" role="img" aria-label="Member photo"></span><span class="member-thumb" role="img" aria-label="Member photo"></span><span class="member-thumb" role="img" aria-label="Member photo"></span>
    <span class="member-thumb" role="img" aria-label="Member photo"></span><span class="member-thumb" role="img" aria-label="Member photo"></span><span class="member-thumb" role="img" aria-label="Member photo"></span>
    <span class="member-thumb" role="img" aria-label="Member photo"></span><span class="member-thumb" role="img" aria-label="Member photo"></span><span class="member-thumb" role="img" aria-label="Member photo"></span>
    <span class="member-thumb" role="img" aria-label="Member photo"></span><span class="member-thumb" role="img" aria-label="Member photo"></span><span class="member-thumb" role="img" aria-label="Member photo"></span>
    <span class="member-thumb" role="img" aria-label="Member photo"></span><span class="member-thumb" role="img" aria-label="Member photo"></span><span class="member-thumb" role="img" aria-label="Member photo"></span>
    <span class="member-thumb" role="img" aria-label="Member photo"></span><span class="member-thumb" role="img" aria-label="Member photo"></span><span class="member-thumb" role="img" aria-label="Member photo"></span>
    <span class="member-thumb" role="img" aria-label="Member photo"></span><span class="member-thumb" role="img" aria-label="Member photo"></span><span class="member-thumb" role="img" aria-label="Member photo"></span>
  </div>

  <section class="abs video-panel"></section>
  <h2 class="abs section-title video-title">VIDEO</h2>
  <div class="abs video-row">
    <div class="video-thumb" role="img" aria-label="Video still of an artist interview"><span class="thumb-play"><svg width="16" height="18" viewBox="0 0 16 18"><polygon points="2,1 15,9 2,17" fill="#333"/></svg>PLAY</span></div>
    <div class="video-thumb" role="img" aria-label="Video still of an artist interview"><span class="thumb-play"><svg width="16" height="18" viewBox="0 0 16 18"><polygon points="2,1 15,9 2,17" fill="#333"/></svg>PLAY</span></div>
    <div class="video-thumb" role="img" aria-label="Video still of an artist interview"><span class="thumb-play"><svg width="16" height="18" viewBox="0 0 16 18"><polygon points="2,1 15,9 2,17" fill="#333"/></svg>PLAY</span></div>
    <div class="video-thumb" role="img" aria-label="Video still of an artist interview"><span class="thumb-play"><svg width="16" height="18" viewBox="0 0 16 18"><polygon points="2,1 15,9 2,17" fill="#333"/></svg>PLAY</span></div>
  </div>

  <div class="abs footer-rule"></div>
  <footer class="abs footer-links">
    <a href="#">Privacy</a><span class="sep">|</span><a href="#">Terms</a><span class="sep">|</span><a href="#">DMCA</a><span class="sep">|</span><a href="#">Video Agreement</a>
    <span class="social"><span aria-label="Social link"></span><span aria-label="Social link"></span></span>
  </footer>

</body>
</html>
```